Etiketten-Design für einen importierten Honig
Zielgruppe
Wir importieren originalen Manuka Honig aus Neuseeland. Der Manuka Honig ist bekannt für seine besonderen Eigenschaften (antibakteriell, etc.). Ein Glas unseres Honigs (500g) kostet zwischen 30 und 150 EUR.
Unsere Zielgruppe sind gesundheitsbewusste Kunden, die wenig preissensibel sind. Überwiegend wird der Manuka Honig im Fachhandel (z.B. Reformhaus, Drogerie, Biomarkt, etc.) verkauft. Der Großteil unserer Kunden ist 30+ Jahre.
Aufgabenstellung
Bei dem Etikett handelt es sich um das erste Produktetikett. Damit ist in der Farbgestaltung noch alles offen. Das Logo und der Name ist jedoch fix.
Das Etikett ist wird auf einem bpa-freien schwarzen Plastikbehälter angebracht. Dieser ist bei Manuka Honigen Standard aufgrund des langen Transports von Neuseeland nach Deutschland (gerne googeln). Der Deckel dieses Behälters ist schwarz.
Nachdem es sich um ein hochpreisiges Produkt handelt, soll das Etikett diese hohe Wertigkeit widerspiegeln. Damit ist eine Veredelung des Etiketts notwendig. Viele Konkurrenten arbeiten mit Gold, alternative Farben sind jedoch auch möglich.
Das Etikett überdeckt drei der vier Seiten des Plastikbehälters (vorne + links + rechts). Die Maße sind 160 mm x 60 mm. Zusätzlich zu den Etikettenmaßen bitte 2 mm Beschnittzugabe je Seite hinzufügen.
Hintergrundinformationen zu unserer Marke:
- Der Markenname lautet Tavolin. Der Markenname leitet sich von der ersten Imkerin Neuseelands ab - Greta Lonfeld. Sie hatte im Jahr 1839 die ersten Bienenstöcke nach Neuseeland gebracht und den ersten Manuka Honig geerntet.
- Unser Logo ist eine Verbindung einer Frau und den neuseeländischen Farn. Dieses Logo stellt also direkt eine Verbindung zu Neuseeland dar.
- Unsere Marke Tavolin ist eine qualitativ hochwertige, luxuriöse und hochpreisige Marke. Genau wie in dem Logo selbst, sollen diese Verbindungen zu Neuseeland, der Natur (Honig ist ein Naturprodukt) und Greta Lonfeld auch auf dem Etikett zu finden sein.
Wonach suchen wir:
- Wir sind auf der Suche nach einem einzigartigen Design, der unseren Honig besonders hervorhebt. Das Etikett soll auffällig sein und uns von anderen unterscheiden. (Eye-catching)
- Eine Veredelung des Etiketts ist Pflicht, da dies für uns die Wertigkeit des Etiketts und des Produktes stark erhöht. In welcher Art die Veredelung durchgeführt wird, ist Ihnen überlassen.
Das dürfen Sie frei wählen:
- Bisher haben..

```html
<!DOCTYPE html>
<html lang="de">
<head>
<meta charset="utf-8">
<title>Tavolin Manuka Honig – Etikett</title>
<link rel="stylesheet" href="https://fonts.googleapis.com/css2?family=Cinzel:wght@400&family=Montserrat:wght@400;500&family=Allura&display=swap">
<style>
  :root {
    --page-bg: #e6e6e6;
    --label-black: #0b0b0b;
    --gold: #c9a45c;
    --gold-light: #e3c27e;
    --blossom: #f2c6d6;
    --blossom-deep: #d98fae;
    --honey: #f5b800;
    --white: #f7f3ee;
  }
  * { margin: 0; padding: 0; box-sizing: border-box; }
  html, body { width: 1200px; height: 1200px; overflow: hidden; }
  body { background: var(--page-bg); position: relative; }

  .label {
    position: absolute; left: 130px; top: 187px;
    width: 940px; height: 826px;
    background: var(--label-black);
    overflow: hidden;
  }
  .frame { position: absolute; inset: 0; }

  .blossom-art {
    position: absolute;
    border-radius: 50%;
    background: radial-gradient(ellipse at 50% 50%, var(--blossom) 0%, var(--blossom-deep) 40%, rgba(201,164,92,0.45) 68%, rgba(11,11,11,0) 72%);
  }
  .blossom-left   { left: 56px;  top: 120px; width: 200px; height: 346px; }
  .blossom-right  { left: 668px; top: 135px; width: 204px; height: 211px; }
  .blossom-bottom { left: 505px; top: 635px; width: 160px; height: 140px; }

  .nz-map {
    position: absolute; left: 685px; top: 520px; width: 165px; height: 190px;
    border-radius: 50%;
    background: radial-gradient(ellipse at 50% 50%, rgba(201,164,92,0.6) 0%, rgba(201,164,92,0.25) 45%, rgba(11,11,11,0) 70%);
  }

  .brand {
    position: absolute; left: 0; width: 940px; top: 55px;
    text-align: center;
  }
  .brand-dot {
    display: block; margin: 0 auto;
    width: 130px; height: 130px; border-radius: 50%;
    background: var(--gold);
  }
  .brand-name {
    margin-top: 38px;
    font-family: "Cinzel", serif; font-weight: 400;
    font-size: 44px; letter-spacing: 12px; line-height: 1;
    padding-left: 12px;
    color: var(--gold);
  }

  .product-title {
    position: absolute; left: 281px; width: 406px; top: 362px;
    text-align: center;
  }
  .title-manuka {
    display: block;
    font-family: "Montserrat", sans-serif; font-weight: 500;
    font-size: 86px; letter-spacing: 1px; line-height: 1;
    color: var(--blossom);
    padding-bottom: 6px;
    border-bottom: 2px solid var(--gold);
  }
  .title-honig {
    display: block; margin-top: 12px;
    font-family: "Cinzel", serif; font-weight: 400;
    font-size: 68px; letter-spacing: 26px; line-height: 1;
    color: var(--gold-light);
    padding-left: 26px; padding-bottom: 8px;
    border-bottom: 2px solid var(--gold);
  }
  .origin {
    position: absolute; left: 14px; width: 940px; top: 538px;
    text-align: center;
    font-family: "Allura", cursive; font-size: 60px; line-height: 1;
    color: var(--white);
  }

  .grade-badge { position: absolute; left: 150px; top: 575px; width: 150px; height: 175px; }
  .grade-text {
    position: absolute; left: 150px; top: 612px; width: 150px;
    text-align: center;
    font-family: "Montserrat", sans-serif; font-weight: 500;
    font-size: 30px; line-height: 1.1; color: var(--label-black);
  }

  .net-weight {
    position: absolute; right: 45px; top: 736px;
    font-family: "Montserrat", sans-serif; font-weight: 400;
    font-size: 30px; color: var(--white);
  }
</style>
</head>
<body>
  <main class="label">
    <div class="blossom-art blossom-left" role="img" aria-label="Manuka-Blütenzweig mit rosa Blüten und goldenen Blättern"></div>
    <div class="blossom-art blossom-right" role="img" aria-label="Manuka-Blütenzweig mit rosa Blüten"></div>
    <div class="blossom-art blossom-bottom" role="img" aria-label="Einzelne rosa Manuka-Blüte"></div>
    <div class="nz-map" role="img" aria-label="Gepunktete Karte von Neuseeland in Gold"></div>

    <svg class="frame" viewBox="0 0 940 826" aria-hidden="true">
      <polyline points="390,118 300,118 120,440 300,760 660,760 840,440 660,118 570,118"
                fill="none" stroke="var(--gold)" stroke-width="3"/>
      <polyline points="380,130 308,130 135,440 308,748 652,748 825,440 652,130 580,130"
                fill="none" stroke="var(--gold)" stroke-width="1.5"/>
    </svg>

    <header class="brand">
      <span class="brand-dot"></span>
      <div class="brand-name">TAVOLIN</div>
    </header>

    <div class="product-title">
      <span class="title-manuka">MANUKA</span>
      <span class="title-honig">HONIG</span>
    </div>
    <p class="origin">Aus Neuseeland</p>

    <svg class="grade-badge" viewBox="0 0 150 175" aria-hidden="true">
      <polygon points="75,4 142,42 142,118 75,156 8,118 8,42" fill="var(--label-black)" stroke="var(--gold)" stroke-width="4"/>
      <polygon points="75,16 132,48 132,112 75,144 18,112 18,48" fill="var(--honey)"/>
      <path d="M75 146 C70 156 68 162 75 170 C82 162 80 156 75 146 Z" fill="var(--honey)"/>
    </svg>
    <div class="grade-text">MGO<br>450+</div>

    <p class="net-weight">℮500 g</p>
  </main>
</body>
</html>
```